Need Business Card for our Indian Grocery Store

Industry/Entity Type

Grocery Store

Contact Information for Business Card

Manoj Baweja
Director

Store Locations:

Ashbury Vale
482 Elm Parade
P: 03 9172 5843

Kelmscott
613 Carlow Road
P: 03 9238 6014

email: kvtmarts@mailnest.example

Requirements
Must have
• Our logo Colours

```html
<!DOCTYPE html>
<html lang="en">
<head>
<meta charset="utf-8">
<title>KVT Marts – Business Card</title>
<link rel="stylesheet" href="https://fonts.googleapis.com/css2?family=Crimson+Pro:wght@600&family=Roboto:wght@400&display=swap">
<style>
  :root {
    --stage: #e9e6e2;
    --card-dark: #1b1b1c;
    --panel-dark: #323233;
    --card-white: #ffffff;
    --brand-red: #e0140f;
    --text-light: #f2f2f2;
    --text-soft: #d9d9d9;
  }
  * { margin: 0; padding: 0; box-sizing: border-box; }
  html, body { width: 1200px; height: 1022px; overflow: hidden; }
  body { background: var(--stage); position: relative; font-family: "Roboto", Arial, sans-serif; }

  .card {
    position: absolute; left: 353px; width: 537px; height: 306px;
    overflow: hidden; box-shadow: 0 4px 10px rgba(0,0,0,.25);
  }
  .card--front { top: 178px; background: var(--card-white); }
  .card--back { top: 508px; background: var(--card-dark); }

  .front-shape { position: absolute; inset: 0; }

  .holder { position: absolute; left: 18px; top: 64px; font-family: "Crimson Pro", Georgia, serif; color: var(--text-light); }
  .holder__name { font-size: 24px; line-height: 26px; font-weight: 600; white-space: nowrap; }
  .holder__role { font-size: 19px; line-height: 20px; font-weight: 600; color: var(--text-soft); }

  .contact { position: absolute; top: 158px; left: 18px; font-size: 12px; line-height: 19px; color: var(--text-light); }
  .contact__store { position: absolute; top: 0; width: 130px; }
  .contact__store--second { left: 119px; }
  .contact__row { display: flex; align-items: center; gap: 5px; white-space: nowrap; }
  .contact__row--indent { padding-left: 21px; }
  .contact__email { position: absolute; top: 57px; left: 0; }
  .icon { width: 16px; height: 14px; flex: none; fill: var(--brand-red); }

  .brand { position: absolute; left: 315px; top: 108px; width: 210px; text-align: center; }
  .brand__name { font-family: "Crimson Pro", Georgia, serif; font-weight: 600; font-size: 46px; line-height: 54px; color: var(--brand-red); white-space: nowrap; }
  .brand__tagline { margin-top: 40px; display: flex; align-items: center; justify-content: center; gap: 6px; font-family: "Crimson Pro", Georgia, serif; font-weight: 600; font-size: 14px; line-height: 16px; color: var(--brand-red); white-space: nowrap; }
  .brand__tagline::before, .brand__tagline::after { content: ""; width: 18px; height: 1px; background: var(--brand-red); flex: none; }

  .back-panel { position: absolute; inset: 0; }
  .back-brand { position: absolute; left: 0; right: 0; top: 116px; text-align: center; font-family: "Crimson Pro", Georgia, serif; font-weight: 600; font-size: 64px; line-height: 70px; color: var(--text-light); white-space: nowrap; }
</style>
</head>
<body>
  <section class="card card--front">
    <svg class="front-shape" viewBox="0 0 537 306" width="537" height="306">
      <path d="M0 0 H205 Q412 153 210 306 H0 Z" fill="var(--brand-red)"/>
      <path d="M0 0 H198 Q392 153 203 306 H0 Z" fill="var(--card-white)"/>
      <path d="M0 0 H190 Q364 153 198 306 H0 Z" fill="var(--card-dark)"/>
    </svg>

    <div class="holder">
      <p class="holder__name">Manoj Baweja</p>
      <p class="holder__role">Director</p>
    </div>

    <div class="contact">
      <div class="contact__store">
        <p class="contact__row"><svg class="icon" viewBox="0 0 16 14"><path d="M8 0 L16 7 H13.5 V14 H9.5 V9.5 H6.5 V14 H2.5 V7 H0 Z"/></svg>Kelmscott</p>
        <p class="contact__row contact__row--indent">613 Carlow Road</p>
        <p class="contact__row"><svg class="icon" viewBox="0 0 16 14"><path d="M2 2 Q8 -1 14 2 L13 5 H11 V4 H5 V5 H3 Z M4 6 H12 L14 13 H2 Z M8 7.5 A2.2 2.2 0 1 0 8 11.9 A2.2 2.2 0 1 0 8 7.5 Z" fill-rule="evenodd"/></svg>03 9238 6014</p>
      </div>
      <div class="contact__store contact__store--second">
        <p class="contact__row"><svg class="icon" viewBox="0 0 16 14"><path d="M8 0 L16 7 H13.5 V14 H9.5 V9.5 H6.5 V14 H2.5 V7 H0 Z"/></svg>Ashbury Vale</p>
        <p class="contact__row contact__row--indent">482 Elm Parade</p>
        <p class="contact__row"><svg class="icon" viewBox="0 0 16 14"><path d="M2 2 Q8 -1 14 2 L13 5 H11 V4 H5 V5 H3 Z M4 6 H12 L14 13 H2 Z M8 7.5 A2.2 2.2 0 1 0 8 11.9 A2.2 2.2 0 1 0 8 7.5 Z" fill-rule="evenodd"/></svg>03 9172 5843</p>
      </div>
      <p class="contact__row contact__email"><svg class="icon" viewBox="0 0 16 14"><path d="M1 2 H15 V12 H1 Z M2.3 3.2 L8 7.8 L13.7 3.2 M2.3 10.8 L6.2 6.6 M13.7 10.8 L9.8 6.6" fill="none" stroke="var(--brand-red)" stroke-width="1.2"/></svg>kvtmarts@mailnest.example</p>
    </div>

    <div class="brand">
      <p class="brand__name">KVT Marts</p>
      <p class="brand__tagline">Fresh Choice Since 2011</p>
    </div>
  </section>

  <section class="card card--back">
    <svg class="back-panel" viewBox="0 0 537 306" width="537" height="306">
      <path d="M40 30 Q268 -6 497 30 Q530 36 530 70 V240 Q530 270 497 276 Q268 312 40 276 Q7 270 7 240 V70 Q7 36 40 30 Z" fill="var(--panel-dark)"/>
    </svg>
    <p class="back-brand">KVT Marts</p>
  </section>
</body>
</html>
```